Zielgruppe
Steuerberatung
Aufgabenstellung
Ich benötige eine Neuerstellung für ein vorhandenes Briefpapier. Bedeutet, eigentlich soll der aktuelle Inhalt neu erstellt werden, da mir die Rohdaten nicht mehr zur Verfügung stehen. Das aktuelle Briefpapier steht als .doc zur Verfügung. Ziel 1:1 Abbildung. Zudem muss die Adresse geändert werden.

```html
<!DOCTYPE html>
<html lang="de">
<head>
<meta charset="utf-8">
<title>Briefpapier Jonas Brenkamp – Steuerberater</title>
<link rel="stylesheet" href="https://fonts.googleapis.com/css2?family=Roboto+Condensed:wght@400;700&display=swap">
<style>
  :root {
    --stage: #808080;
    --paper: #ffffff;
    --ink: #111111;
    --mark: #4a4a4a;
    --watermark: #d9d9d9;
  }
  * { margin: 0; padding: 0; box-sizing: border-box; }
  html, body { width: 1200px; height: 1200px; overflow: hidden; }
  body {
    background: var(--stage);
    font-family: "Roboto Condensed", "Arial Narrow", sans-serif;
    color: var(--ink);
    position: relative;
  }
  .sheet {
    position: absolute;
    left: 240px; top: 91px;
    width: 720px; height: 1018px;
    background: var(--paper);
    overflow: hidden;
  }
  .brand {
    position: absolute;
    left: 523px; top: 57px;
    display: flex; align-items: center; gap: 7px;
  }
  .brand-square {
    width: 14px; height: 14px;
    border: 1px solid var(--mark);
  }
  .brand-name {
    font-size: 15px; font-weight: 700; color: var(--mark);
    letter-spacing: 0.2px;
  }
  .sender-line {
    position: absolute;
    left: 69px; top: 153px;
    font-size: 8.5px; color: var(--ink);
    white-space: nowrap;
  }
  .contact {
    position: absolute;
    left: 523px; top: 151px;
    font-size: 11px; line-height: 14.5px;
  }
  .contact .row { display: flex; white-space: nowrap; }
  .contact .label { width: 25px; flex-shrink: 0; }
  strong { font-weight: 700; }
  .watermark {
    position: absolute;
    right: 24px; top: 862px;
    font-size: 54px; font-weight: 700;
    color: var(--watermark);
    line-height: 1;
    white-space: nowrap;
    z-index: 0;
  }
  .legal {
    position: absolute;
    left: 69px; top: 944px;
    font-size: 10.5px; line-height: 14.5px;
    white-space: nowrap;
    z-index: 1;
  }
</style>
</head>
<body>
  <main class="sheet">
    <div class="brand">
      <span class="brand-square"></span>
      <span class="brand-name">Brenkamp</span>
    </div>

    <p class="sender-line">Jonas Brenkamp&nbsp; |&nbsp; Lerchenstr. 18&nbsp; |&nbsp; 30161 Hannover</p>

    <div class="contact">
      <p><strong>Jonas Brenkamp</strong> | Steuerberater</p>
      <p class="row"><span class="label">Tel.:</span>+49 (0) 170 - 55 20 318</p>
      <p class="row"><span class="label">Fax.:</span>+49 (0) 511 - 12 34 56 78</p>
      <p class="row"><span class="label">Mail:</span>info@kanzlei-brenkamp.de</p>
      <p class="row"><span class="label">Web:</span>www.kanzlei-brenkamp.de</p>
    </div>

    <div class="watermark" aria-hidden="true">Brenkamp</div>

    <footer class="legal">
      <p><strong>Jonas Brenkamp</strong> | Steuerberater</p>
      <p>Lerchenstr. 18&nbsp; |&nbsp; 30161 Hannover&nbsp; |&nbsp; Zuständige Aufsichtsbehörde: Steuerberaterkammer Nordland -Körperschaft des öffentlichen Rechts-</p>
      <p>Zuständiges Finanzamt: Finanzamt Nordstadt, Steuernummer: 00/000/12345&nbsp; |&nbsp; Bankverbindung: DE 00 1234 5678 9012 3456 78 BIC: MUSTDEXXX</p>
    </footer>
  </main>
</body>
</html>
```